Picture Ads

We need some banner ads for our home business opportunity, we are evolving from text to picture ads. I have added some examples of what other distributors are using. We are looking for something really eye catching with some good key words and nice bright colours and to include our photo (attached)
Key words to include:
Booming online business
Personal Development and Leadership Industry
Earn an executive income from home
Simple 3 step system
Make up to $5,000 per sale
Not MLM
The size needs to be: 1000 x 35 pixels
13.9 x 4.75 Inches
35.3 x 11.1 cm
I think different platforms accept different sizes, not too familiar with it yet, any guidance welcome. I've clicked project for 2 days if that is to prioritise the order?
Many thanks,
Maren

Industry/Entity Type

Business

```html
<!DOCTYPE html>
<html lang="en">
<head>
<meta charset="utf-8">
<title>Booming Online Business – Banner Ads</title>
<link href="https://fonts.googleapis.com/css2?family=Yanone+Kaffeesatz:wght@700&family=Ubuntu:ital,wght@0,500;0,700;1,500&family=Caveat:wght@500&display=swap" rel="stylesheet">
<style>
  :root {
    --stage: #3d3d3d;
    --white: #ffffff;
    --gold-left: #f9c800;
    --gold-right: #f2a400;
    --gold-title: #3b1a0d;
    --gold-frame: #e81010;
    --lime-left: #b6cc00;
    --lime-right: #e9c400;
    --lime-title: #8e2c10;
    --lime-frame: #f7931e;
    --band: #ffff3a;
    --ink: #1e1408;
    --cta-top: #f7a030;
    --cta-bottom: #e8640c;
    --cta-text: #3b1a0d;
    --splash: rgba(150, 60, 10, 0.55);
  }
  * { margin: 0; padding: 0; box-sizing: border-box; }
  html, body {
    width: 1200px; height: 823px; overflow: hidden;
    background: var(--stage);
  }
  .banner {
    position: absolute; left: 34px; width: 1141px; height: 357px; overflow: hidden;
    --title: var(--gold-title);
    --frame: var(--gold-frame);
    --tick: var(--gold-title);
  }
  .banner--gold {
    top: 38px;
    background:
      radial-gradient(ellipse 260px 150px at 1080px 300px, var(--splash), transparent 70%),
      radial-gradient(ellipse 500px 260px at 900px 120px, rgba(255,250,120,0.45), transparent 70%),
      linear-gradient(90deg, var(--gold-left) 0%, #fbd400 45%, var(--gold-right) 100%);
  }
  .banner--lime {
    top: 435px;
    --title: var(--lime-title);
    --frame: var(--lime-frame);
    --tick: var(--lime-title);
    background:
      radial-gradient(ellipse 260px 150px at 1080px 300px, var(--splash), transparent 70%),
      radial-gradient(ellipse 500px 260px at 900px 120px, rgba(255,250,120,0.45), transparent 70%),
      linear-gradient(90deg, var(--lime-left) 0%, #c8d200 45%, var(--lime-right) 100%);
  }
  .portrait-frame { position: absolute; left: 0; top: 0; width: 320px; height: 357px; }
  .portrait-frame .outer { fill: var(--white); }
  .portrait-frame .band { fill: var(--frame); }
  .signature {
    position: absolute; left: 66px; top: 268px;
    font: 500 30px 'Caveat', cursive; color: #2a1a10;
    transform: rotate(-10deg); transform-origin: left center;
    text-shadow: 0 0 6px #fff, 0 0 6px #fff, 0 0 3px #fff;
    white-space: nowrap;
  }
  .headline {
    position: absolute; left: 376px; top: 12px;
    font: 700 92px/1 'Yanone Kaffeesatz', sans-serif; color: var(--title);
    letter-spacing: 0.5px; white-space: nowrap;
    text-shadow:
      -2px -2px 0 #fff, 2px -2px 0 #fff, -2px 2px 0 #fff, 2px 2px 0 #fff,
      0 -3px 0 #fff, 0 3px 0 #fff, -3px 0 0 #fff, 3px 0 0 #fff,
      4px 6px 6px rgba(0,0,0,0.45);
  }
  .tagline {
    position: absolute; left: 390px; top: 128px; width: 730px; height: 48px;
    background: linear-gradient(90deg, rgba(255,255,58,0) 0%, var(--band) 14%, var(--band) 80%, rgba(255,255,58,0) 100%);
    font: 700 38px/48px 'Yanone Kaffeesatz', sans-serif; color: var(--ink);
    text-align: center;
  }
  .benefits { position: absolute; left: 402px; top: 196px; list-style: none; }
  .benefits li {
    display: flex; align-items: center; height: 38px;
    font: 500 26px 'Ubuntu', sans-serif; color: var(--ink); white-space: nowrap;
  }
  .benefits svg { width: 24px; height: 24px; margin-right: 12px; flex: none; }
  .benefits .tick-bg { fill: var(--tick); }
  .cta { position: absolute; left: 912px; top: 270px; width: 212px; height: 80px; }
  .cta svg { position: absolute; inset: 0; }
  .cta-label {
    position: absolute; left: 28px; right: 8px; top: 14px; text-align: center;
    font: 700 26px/1 'Ubuntu', sans-serif; color: var(--cta-text);
  }
  .cta-sub {
    position: absolute; left: 28px; right: 8px; top: 44px; text-align: center;
    font: italic 500 19px/1 'Ubuntu', sans-serif; color: var(--white);
  }
</style>
</head>
<body>

<section class="banner banner--gold">
  <svg class="portrait-frame" viewBox="0 0 320 357">
    <defs>
      <linearGradient id="photo-tone-a" x1="0" y1="0" x2="1" y2="1">
        <stop offset="0" stop-color="#5a3a2c"/>
        <stop offset="0.5" stop-color="#c9917a"/>
        <stop offset="1" stop-color="#2a1c18"/>
      </linearGradient>
    </defs>
    <path class="outer" d="M140,0 C120,70 36,110 36,185 C36,250 100,290 140,305 C148,325 135,345 125,357 L195,357 C185,345 172,325 180,305 C220,290 284,250 284,185 C284,110 200,70 180,0 Z"/>
    <path class="band" d="M152,0 C135,75 58,115 58,185 C58,240 115,275 150,292 C155,320 150,345 145,357 L175,357 C170,345 165,320 170,292 C205,275 262,240 262,185 C262,115 185,75 168,0 Z"/>
    <path role="img" aria-label="Photo of the two business partners smiling together" fill="url(#photo-tone-a)" d="M160,20 C145,90 76,125 76,185 C76,235 125,262 160,275 C195,262 244,235 244,185 C244,125 175,90 160,20 Z"/>
  </svg>
  <div class="signature">Maren and Tessa Harlow</div>
  <h1 class="headline">Booming Online Business</h1>
  <p class="tagline">Earn an executive income from home</p>
  <ul class="benefits">
    <li><svg viewBox="0 0 24 24"><circle class="tick-bg" cx="12" cy="12" r="12"/><path d="M6.5 12.5 L10.5 16.5 L17.5 8" fill="none" stroke="#fff" stroke-width="3" stroke-linecap="round" stroke-linejoin="round"/></svg>Personal Development and Leadership Industry</li>
    <li><svg viewBox="0 0 24 24"><circle class="tick-bg" cx="12" cy="12" r="12"/><path d="M6.5 12.5 L10.5 16.5 L17.5 8" fill="none" stroke="#fff" stroke-width="3" stroke-linecap="round" stroke-linejoin="round"/></svg>Make Up To $5,000 Per Sale</li>
    <li><svg viewBox="0 0 24 24"><circle class="tick-bg" cx="12" cy="12" r="12"/><path d="M6.5 12.5 L10.5 16.5 L17.5 8" fill="none" stroke="#fff" stroke-width="3" stroke-linecap="round" stroke-linejoin="round"/></svg>Simple 3 Step System</li>
    <li><svg viewBox="0 0 24 24"><circle class="tick-bg" cx="12" cy="12" r="12"/><path d="M6.5 12.5 L10.5 16.5 L17.5 8" fill="none" stroke="#fff" stroke-width="3" stroke-linecap="round" stroke-linejoin="round"/></svg>Not MLM</li>
  </ul>
  <a class="cta">
    <svg viewBox="0 0 212 80">
      <defs>
        <linearGradient id="cta-fill-a" x1="0" y1="0" x2="0" y2="1">
          <stop offset="0" stop-color="#f7a030"/><stop offset="1" stop-color="#e8640c"/>
        </linearGradient>
      </defs>
      <path d="M0,12 L22,0 L22,12 Z" fill="#b4460a"/>
      <rect x="18" y="10" width="190" height="68" rx="8" fill="url(#cta-fill-a)" stroke="#c85208" stroke-width="2"/>
      <path d="M0,12 L22,12 L22,40 Z" fill="#f08a20"/>
    </svg>
    <span class="cta-label">CLICK HERE</span>
    <span class="cta-sub">For More Info</span>
  </a>
</section>

<section class="banner banner--lime">
  <svg class="portrait-frame" viewBox="0 0 320 357">
    <defs>
      <linearGradient id="photo-tone-b" x1="0" y1="0" x2="1" y2="1">
        <stop offset="0" stop-color="#5a3a2c"/>
        <stop offset="0.5" stop-color="#c9917a"/>
        <stop offset="1" stop-color="#2a1c18"/>
      </linearGradient>
    </defs>
    <path class="outer" d="M140,0 C120,70 36,110 36,185 C36,250 100,290 140,305 C148,325 135,345 125,357 L195,357 C185,345 172,325 180,305 C220,290 284,250 284,185 C284,110 200,70 180,0 Z"/>
    <path class="band" d="M152,0 C135,75 58,115 58,185 C58,240 115,275 150,292 C155,320 150,345 145,357 L175,357 C170,345 165,320 170,292 C205,275 262,240 262,185 C262,115 185,75 168,0 Z"/>
    <path role="img" aria-label="Photo of the two business partners smiling together" fill="url(#photo-tone-b)" d="M160,20 C145,90 76,125 76,185 C76,235 125,262 160,275 C195,262 244,235 244,185 C244,125 175,90 160,20 Z"/>
  </svg>
  <div class="signature">Maren and Tessa Harlow</div>
  <h1 class="headline">Booming Online Business</h1>
  <p class="tagline">Earn an executive income from home</p>
  <ul class="benefits">
    <li><svg viewBox="0 0 24 24"><circle class="tick-bg" cx="12" cy="12" r="12"/><path d="M6.5 12.5 L10.5 16.5 L17.5 8" fill="none" stroke="#fff" stroke-width="3" stroke-linecap="round" stroke-linejoin="round"/></svg>Personal Development and Leadership Industry</li>
    <li><svg viewBox="0 0 24 24"><circle class="tick-bg" cx="12" cy="12" r="12"/><path d="M6.5 12.5 L10.5 16.5 L17.5 8" fill="none" stroke="#fff" stroke-width="3" stroke-linecap="round" stroke-linejoin="round"/></svg>Make Up To $5,000 Per Sale</li>
    <li><svg viewBox="0 0 24 24"><circle class="tick-bg" cx="12" cy="12" r="12"/><path d="M6.5 12.5 L10.5 16.5 L17.5 8" fill="none" stroke="#fff" stroke-width="3" stroke-linecap="round" stroke-linejoin="round"/></svg>Simple 3 Step System</li>
    <li><svg viewBox="0 0 24 24"><circle class="tick-bg" cx="12" cy="12" r="12"/><path d="M6.5 12.5 L10.5 16.5 L17.5 8" fill="none" stroke="#fff" stroke-width="3" stroke-linecap="round" stroke-linejoin="round"/></svg>Not MLM</li>
  </ul>
  <a class="cta">
    <svg viewBox="0 0 212 80">
      <defs>
        <linearGradient id="cta-fill-b" x1="0" y1="0" x2="0" y2="1">
          <stop offset="0" stop-color="#f7a030"/><stop offset="1" stop-color="#e8640c"/>
        </linearGradient>
      </defs>
      <path d="M0,12 L22,0 L22,12 Z" fill="#b4460a"/>
      <rect x="18" y="10" width="190" height="68" rx="8" fill="url(#cta-fill-b)" stroke="#c85208" stroke-width="2"/>
      <path d="M0,12 L22,12 L22,40 Z" fill="#f08a20"/>
    </svg>
    <span class="cta-label">CLICK HERE</span>
    <span class="cta-sub">For More Info</span>
  </a>
</section>

</body>
</html>
```